Advertising Flyer

I'm looking for a one page flyer I can use for magazine advertising as well as in PDF format for email correspondence to potential clients. I attached an example from another company that I liked. The company website can be found at www.lurvin-dax.com. The attached Services and Contact/About pages should have all the information needed. Imagery of oil rigs, derricks, and/or pipelines is expected.

Target Market(s)

Energy Industry

Industry/Entity Type

Advertising

Font styles to use
Sans Serif
Other font styles liked:
• same as website

Requirements
Must have
• Contact Info
• List of Services
• About Company Paragraph

```html
<!DOCTYPE html>
<html lang="en">
<head>
<meta charset="utf-8">
<title>Lurvin Dax Group – Advertising Flyer</title>
<link href="https://fonts.googleapis.com/css2?family=Open+Sans:wght@400;600;700;800&display=swap" rel="stylesheet">
<style>
  :root{
    --stage:#5b5b5d;
    --brand-blue:#1d8fc4;
    --ink:#1b1b1b;
    --band:#0b0c0e;
    --panel:rgba(255,255,255,0.88);
    --white:#ffffff;
    --muted:#d9dde0;
  }
  *{box-sizing:border-box;margin:0;padding:0}
  html,body{width:1200px;height:927px;overflow:hidden}
  body{background:var(--stage);font-family:"Open Sans",Arial,sans-serif;position:relative}

  .flyer{position:absolute;left:270px;top:36px;width:660px;height:855px;background:var(--white);overflow:hidden;box-shadow:0 6px 24px rgba(0,0,0,.35)}

  .hero-photo{position:absolute;left:0;top:0;width:660px;height:468px;
    background:linear-gradient(160deg,#f4f8fa 0%,#cfe3ec 30%,#6fa9c2 55%,#2f6f8c 78%,#10313f 100%)}
  .lower-photo{position:absolute;left:0;top:472px;width:660px;height:288px;
    background:linear-gradient(100deg,#7fa6ba 0%,#b9d0dc 30%,#e6eef2 60%,#f3f6f8 100%)}
  .rule{position:absolute;left:0;top:468px;width:660px;height:4px;background:var(--brand-blue)}

  .brand{position:absolute;right:40px;top:46px;display:flex;align-items:center;gap:12px}
  .brand-dot{width:34px;height:34px;border-radius:50%;background:var(--brand-blue)}
  .brand-name{font-size:34px;font-weight:600;color:var(--brand-blue);letter-spacing:1px}

  .about{position:absolute;left:290px;top:128px;width:310px;height:310px;border-radius:50%;
    background:var(--white);border:5px solid var(--brand-blue);box-shadow:0 4px 14px rgba(0,0,0,.3);
    display:flex;align-items:center;justify-content:center;padding:0 46px;text-align:center}
  .about p{font-size:13px;line-height:1.45;color:var(--ink)}

  .services{position:absolute;left:40px;top:472px;width:580px;height:288px;background:var(--panel);
    padding:10px 22px;display:flex;gap:26px}
  .services h2{font-size:22px;font-weight:800;color:var(--brand-blue);margin-bottom:2px;letter-spacing:.5px;line-height:1.3}
  .col{flex:1}
  .group{margin-bottom:5px}
  .group-title{font-size:13px;font-weight:700;color:var(--ink);display:flex;align-items:center;gap:6px;line-height:1.35}
  .group-title::before{content:"";width:7px;height:7px;background:var(--brand-blue);transform:rotate(45deg);flex:none}
  .group ul{list-style:none;padding-left:24px}
  .group li{font-size:11.5px;line-height:1.32;color:var(--ink);position:relative}
  .group li::before{content:"•";position:absolute;left:-10px}
  .col.right{padding-top:8px}

  .band{position:absolute;left:0;top:760px;width:660px;height:95px;background:var(--band);border-top:4px solid var(--brand-blue)}
  .person{position:absolute;left:36px;bottom:16px;color:var(--white)}
  .person .name{font-size:30px;font-weight:800;line-height:1.05}
  .person .role{font-size:15px;color:var(--muted);margin-left:150px}
  .contact{position:absolute;right:40px;top:8px;color:var(--white);font-size:12.5px;line-height:1.45}
  .contact .phone{font-size:17px;font-weight:700}
  .contact li{list-style:none;display:flex;align-items:center;gap:8px}
  .contact svg{width:12px;height:12px;fill:var(--brand-blue);flex:none}
</style>
</head>
<body>
  <main class="flyer">
    <div class="hero-photo" role="img" aria-label="Photo of oil pumpjacks silhouetted against a blue sky"></div>
    <div class="lower-photo" role="img" aria-label="Photo of steel pipeline valves, pipework and storage tanks"></div>
    <div class="rule"></div>

    <div class="brand">
      <span class="brand-dot"></span>
      <span class="brand-name">Lurvin Dax Group</span>
    </div>

    <section class="about">
      <p>Lurvin Dax Group, Inc. is a full service land firm dedicated to providing quality land services nation-wide to the oil and gas industry, pipeline companies, attorneys, public agencies, and land and mineral owners. We pride ourselves on providing the highest level of experience and dedication while completing the job in an accurate, timely, and cost-efficient manner.</p>
    </section>

    <section class="services">
      <div class="col left">
        <h2>SERVICES</h2>
        <div class="group">
          <div class="group-title">Oil And Gas</div>
          <ul><li>Surface and Mineral Title Research</li><li>Lease and Mineral Acquisition</li><li>Lease Checks and Take Offs</li></ul>
        </div>
        <div class="group">
          <div class="group-title">Right Of Way</div>
          <ul><li>SurfaceTitle and Acquisition</li><li>Surface Site Negotiations and Agreements</li><li>Right of Way Engineering</li></ul>
        </div>
        <div class="group">
          <div class="group-title">Seismic</div>
          <ul><li>Surface and Mineral Permitting</li><li>Working Interest Permitting</li><li>Damage Settlements</li></ul>
        </div>
      </div>
      <div class="col right">
        <div class="group"><div class="group-title">Abstracting</div></div>
        <div class="group"><div class="group-title">GIS Solutions - Secure Online Maps</div></div>
        <div class="group">
          <div class="group-title">Title Curative</div>
          <ul><li>Conveyances, Assignments and Transfers</li><li>Title Conflict Resolution</li><li>Probate Matters</li></ul>
        </div>
        <div class="group"><div class="group-title">Due Diligence and File Management</div></div>
        <div class="group"><div class="group-title">Regulatory Agency Permitting</div></div>
      </div>
    </section>

    <footer class="band">
      <div class="person">
        <div class="name">Dale Horvath, RPL</div>
        <div class="role">President</div>
      </div>
      <ul class="contact">
        <li class="phone"><svg viewBox="0 0 12 12"><path d="M2 1h2.5l1 3-1.5 1a6 6 0 0 0 3 3l1-1.5 3 1V11a1 1 0 0 1-1 1A10 10 0 0 1 1 2a1 1 0 0 1 1-1z"/></svg>337-555-0142</li>
        <li><svg viewBox="0 0 12 12"><path d="M6 0a4 4 0 0 1 4 4c0 3-4 8-4 8S2 7 2 4a4 4 0 0 1 4-4zm0 2.5a1.5 1.5 0 1 0 0 3 1.5 1.5 0 0 0 0-3z"/></svg>2280 W. Arden Pl., Baton Rouge, LA 70810</li>
        <li><svg viewBox="0 0 12 12"><path d="M0 2h12v8H0zM1 3l5 4 5-4v-.2H1z" fill-rule="evenodd"/></svg>dale@lurvin-dax.com</li>
        <li><svg viewBox="0 0 12 12"><circle cx="6" cy="6" r="5.5"/><path d="M1 6h10M6 .5c-2 2-2 9 0 11M6 .5c2 2 2 9 0 11" stroke="#0b0c0e" stroke-width=".8" fill="none"/></svg>www.lurvin-dax.com</li>
      </ul>
    </footer>
  </main>
</body>
</html>
```